Business card design needed

I am a nutritionist and fitness instructor and I need a business card designed for my company SowGrowThrive. I provide nutrition education services such as consultations, cooking demonstrations, workshops, and supermarket tours. I also provide fitness instruction and training to clients to help overhaul their lifestyle.

I would like to see designs that have a natural, organic, feel using earthy colours. I would like to have cards printed on recycled paper.

I would prefer a 2 sided card. Front side with just the business name Sow Grow Thrive and underneath Nutrition Health Fitness. The second side to have the contact details.

The final design should communicate health and wellness through eating organic wholefoods and being physically active.

Although I have this idea, I would be open to see other suggestions that have a similar look and feel.
Updates

Target Market(s)

people interested in being healthier, women wanting to loose weight, mothers wanting to be healthier for their families

Industry/Entity Type

Nutrition

Contact Information for Business Card

Nadia Crewe
Nutritionist and Personal Trainer
M 0417582936
E sowgrowthrivenutrition@mailbox-example.net

Logo Text

SowGrowThrive (underneath) Nutrition Health Fitness

Logo styles of interest
Wordmark Logo
Requirements
Nice to have
• I like the idea of having the letters of SowGrowThrive spelt out with food such as grains, nuts, seeds, legumes, fruit etc. For example close up images of cherry tomatoes, chia seeds, kidney beans, chickpeas, blue berries, raspberries, brown rice - lots of different colours and textures. Continuing playing on the idea of the book cover Dig Rest Glow.

food is important - I am not selling supplements rather I am promoting the enjoyment of healthy wholefoods so food is important to the look and feel of the design
Should not have
• cartoon images
images associated with body building or supplements
fruit or dumb bells with tape measures around them
clichés for weight loss such as scales and tape measures
I don't want to look like other typical wellness services such as massage or spa services

```html
<!DOCTYPE html>
<html lang="en">
<head>
<meta charset="utf-8">
<title>SowGrowThrive – Business Card</title>
<link href="https://fonts.googleapis.com/css2?family=Arimo:wght@400;700&display=swap" rel="stylesheet">
<style>
  :root {
    --backdrop: #e6e7e9;
    --card: #ffffff;
    --brand-brown: #7a4c22;
    --tagline: #6a5224;
    --name-olive: #8b7d32;
    --title-red: #a3262a;
    --contact: #7c5a22;
    --bean: #8e1c22;
    --raspberry: #e23a48;
    --pistachio: #d9c6a0;
    --tomato: #e0261c;
  }
  html, body {
    margin: 0;
    width: 1200px;
    height: 1000px;
    overflow: hidden;
    background: var(--backdrop);
    font-family: "Arimo", Arial, sans-serif;
  }
  .canvas { position: relative; width: 1200px; height: 1000px; }
  .card {
    position: absolute;
    width: 697px;
    height: 402px;
    background: var(--card);
    box-shadow: 3px 4px 6px rgba(0,0,0,0.35);
    overflow: hidden;
  }
  .card--front { left: 73px; top: 73px; }
  .card--back { left: 319px; top: 519px; }

  .wordmark {
    position: absolute;
    margin: 0;
    font-weight: 700;
    color: var(--brand-brown);
    letter-spacing: -1px;
    line-height: 1;
    white-space: nowrap;
  }
  .tagline {
    position: absolute;
    margin: 0;
    font-weight: 700;
    color: var(--tagline);
    letter-spacing: 2.4px;
    white-space: nowrap;
  }
  .card--front .wordmark { left: 156px; top: 160px; font-size: 56px; }
  .card--front .tagline { left: 157px; top: 223px; font-size: 15.5px; }
  .card--back .wordmark { left: 46px; top: 273px; font-size: 42px; }
  .card--back .tagline { left: 46px; top: 323px; font-size: 13px; letter-spacing: 1.9px; }

  .food { position: absolute; }
  .food--beans {
    left: -10px; top: 305px; width: 230px; height: 130px;
    border-radius: 50% 50% 0 0 / 70% 70% 0 0;
    background: radial-gradient(ellipse at 45% 40%, #b4343a 0%, var(--bean) 55%, #5e1015 100%);
  }
  .food--raspberries {
    left: 500px; top: 222px; width: 205px; height: 190px;
    border-radius: 60% 0 0 0 / 50% 0 0 0;
    background: radial-gradient(ellipse at 55% 60%, #d92a3a 0%, var(--raspberry) 45%, rgba(240,110,120,0.5) 75%, rgba(255,255,255,0) 100%);
  }
  .food--pistachios {
    left: -4px; top: 144px; width: 178px; height: 118px;
    border-radius: 0 60% 45% 0 / 0 55% 50% 0;
    background: radial-gradient(ellipse at 40% 45%, #efe3c8 0%, var(--pistachio) 50%, #a98e5c 100%);
  }
  .food--tomatoes {
    left: 448px; top: 186px; width: 238px; height: 180px;
    border-radius: 50%;
    background: radial-gradient(ellipse at 45% 42%, #ff5a40 0%, var(--tomato) 45%, #a8140e 80%, rgba(255,255,255,0) 100%);
  }

  .contact-block { position: absolute; left: 46px; top: 34px; }
  .person-name {
    margin: 0;
    font-size: 20px;
    font-weight: 700;
    color: var(--name-olive);
    letter-spacing: 2.4px;
  }
  .person-role {
    margin: 5px 0 0;
    font-size: 16px;
    font-weight: 700;
    color: var(--title-red);
    letter-spacing: 2.2px;
  }
  .contact-list { list-style: none; margin: 12px 0 0; padding: 0; }
  .contact-list li {
    display: flex;
    align-items: center;
    gap: 3px;
    font-size: 13px;
    font-weight: 700;
    color: var(--contact);
    letter-spacing: 2px;
    line-height: 19px;
  }
  .contact-list svg { width: 13px; height: 13px; flex: none; }
</style>
</head>
<body>
<main class="canvas">

  <section class="card card--front" aria-label="Card front">
    <div class="food food--beans" role="img" aria-label="Photo of a pile of red kidney beans"></div>
    <div class="food food--raspberries" role="img" aria-label="Photo of fresh raspberries"></div>
    <h1 class="wordmark">SowGrowThrive</h1>
    <p class="tagline">Nutrition Health Fitness</p>
  </section>

  <section class="card card--back" aria-label="Card back">
    <div class="contact-block">
      <h2 class="person-name">Nadia Crewe</h2>
      <p class="person-role">Nutritionist and Personal Trainer</p>
      <ul class="contact-list">
        <li>
          <svg viewBox="0 0 14 14" aria-hidden="true">
            <path d="M4 1.5 L6 4.5 L4.8 6 Q6 8.5 8 9.2 L9.5 8 L12.5 10 L11 12.5 Q5 12 1.8 3.5 Z" fill="var(--contact)"/>
          </svg>
          0417582936
        </li>
        <li>
          <svg viewBox="0 0 14 14" aria-hidden="true">
            <circle cx="7" cy="7" r="6" fill="none" stroke="var(--contact)" stroke-width="1.5"/>
            <rect x="3.6" y="4.6" width="6.8" height="4.8" fill="none" stroke="var(--contact)" stroke-width="1.1"/>
            <path d="M3.6 4.8 L7 7.4 L10.4 4.8" fill="none" stroke="var(--contact)" stroke-width="1.1"/>
          </svg>
          sowgrowthrivenutrition@mailbox-example.net
        </li>
      </ul>
    </div>
    <div class="food food--pistachios" role="img" aria-label="Photo of a heap of pistachio nuts"></div>
    <div class="food food--tomatoes" role="img" aria-label="Photo of three cherry tomatoes on the vine"></div>
    <p class="wordmark">SowGrowThrive</p>
    <p class="tagline">Nutrition Health Fitness</p>
  </section>

</main>
</body>
</html>
```